8-page Visitor's Guide for Private Wildlife Ranch

We need a Visitor's Guide for Private Wildlife Ranch, where we can include important information for the clients during their stay as well as the many activities we and surrounding businesses have to offer... we are looking to keep it in line with our current web look and feel, as well as some of the included supporting documents, our rack card and our current tribe-fold brochure... I will be looking to update these as well in the near future with a supporting design... just looking for something a little more eye catching and up to date!

http:// mbxq.example.org/leaflets/qrsleaf/files/mbx_lf_q7111_2222zz.

the pdf above is something we really like!!!!

Im sure you are going to need more photos, but I was limited to what I could upload!

www. klcreeksidelodge. com is our website

Info about us: Are you looking for a truly unique Texas experience? K.L. Creekside Lodge is THE place! Whether you are looking for a day trip, a weekend adventure, or a place to host your next event or corporate retreat, join us at K.L. Creekside Lodge.

No matter what your needs and interests are, we offer a wide variety of activities to suit any group. K.L. Creekside Lodge has been the chosen destination for many weddings, events, and corporate retreats.

Target Market(s)

Tourism/Travel

Industry/Entity Type

Tourism

Font styles to use
Other font styles liked:
• Plantagenet Cherokee

Colors
fff3d1
ffffff

Requirements
Must have
• I have included a pdf with a lot of the text that I want.....
• Pages to include: Cover page, Important Information, Welcome Letter/Map, What to do while here, special events at the ranch, lodging options, things you might see during your stay, and a page for ads from local businesses
• colors
• 3e2a05 dark brown
• d2c0a4 light brown
• f3f2f1 light light brown
• font:
• Plantagenet Cherokee
Nice to have
• I want it to have an easy to read, rustic ranch look like with the feel of our website, but fun and exciting to make it inviting and welcoming
Should not have
• ehh pretty open to most anything but bright colors

```html
<!DOCTYPE html>
<html lang="en">
<head>
<meta charset="utf-8">
<title>K.L. Creekside Lodge – Visitor's Guide Spread</title>
<link rel="stylesheet" href="https://fonts.googleapis.com/css2?family=Montserrat:wght@700;800&family=Lora:wght@400;600&display=swap">
<style>
  :root {
    --cream: #fff3d1;
    --paper: #ffffff;
    --brown-dark: #3e2a05;
    --brown-light: #d2c0a4;
    --brown-pale: #f3f2f1;
    --ink: #1e1a14;
    --sky-top: #f4f4f2;
    --sky-low: #d9dcdc;
    --stone: #8b8073;
    --ground: #c9c5bc;
  }
  * { margin: 0; padding: 0; box-sizing: border-box; }
  html, body { width: 1200px; height: 900px; overflow: hidden; }
  body { background: var(--cream); position: relative; font-family: "Lora", Georgia, serif; color: var(--ink); }

  .page {
    position: absolute; top: 42px; width: 505px; height: 786px;
    background: var(--paper); overflow: hidden;
    box-shadow: 3px 4px 6px rgba(0,0,0,0.18);
  }
  .page--amenities { left: 84px; }
  .page--activities { left: 614px; }

  .page-title { position: absolute; top: 0; left: 0; width: 100%; height: 130px; }
  .page-title__band { position: absolute; top: 67px; height: 20px; background: var(--brown-light); }
  .page-title__main {
    position: absolute; top: 40px; font-family: "Montserrat", Arial, sans-serif;
    font-weight: 800; font-size: 44px; color: var(--brown-dark); line-height: 1; letter-spacing: -0.5px;
  }
  .page-title__kicker {
    position: absolute; top: 40px; font-family: "Montserrat", Arial, sans-serif;
    font-weight: 700; font-size: 18px; color: var(--brown-dark); line-height: 1;
  }

  .watermark {
    position: absolute; left: 0; width: 100%; text-align: center;
    font-family: "Lora", Georgia, serif; font-weight: 600; color: var(--brown-pale);
    font-size: 40px; letter-spacing: 3px; top: 470px; transform: rotate(-14deg);
  }

  .feature-photo {
    position: absolute; left: 53px; top: 151px; width: 150px; height: 150px; border-radius: 50%;
    background: radial-gradient(circle at 50% 60%, #9b3a3a 0%, #7a2b2e 40%, #8c6a4e 70%, #cfc2b0 100%);
    box-shadow: 0 0 0 4px #e4dccf;
  }
  .feature-item {
    position: absolute; left: 228px; top: 208px; font-size: 30px; color: var(--ink);
  }
  .feature-item::before { content: "•"; font-size: 20px; margin-right: 12px; vertical-align: 5px; }

  .amenity { position: absolute; width: 140px; text-align: center; }
  .amenity__ring {
    width: 110px; height: 110px; margin: 0 auto; border-radius: 50%;
    border: 8px solid var(--brown-light); background: var(--paper);
    display: flex; align-items: center; justify-content: center;
  }
  .amenity__ring svg { width: 60px; height: 60px; }
  .amenity__label { margin-top: 7px; font-size: 14px; color: var(--ink); }

  .scene-photo {
    position: absolute; left: 0; bottom: 0; width: 505px; height: 260px;
    background: linear-gradient(180deg, rgba(255,255,255,0) 0%, var(--sky-top) 18%, var(--sky-low) 45%, var(--stone) 62%, #9a8f80 82%, var(--ground) 100%);
  }

  .activity { position: absolute; left: 0; width: 405px; }
  .activity__tab {
    display: block; height: 20px; width: 186px; background: var(--brown-light);
    border-radius: 0 10px 10px 0; padding-left: 70px;
    font-size: 14px; line-height: 20px; color: var(--ink);
  }
  .activity__tab--wide { width: 298px; }
  .activity__text {
    margin-left: 70px; margin-top: 2px; font-size: 12.2px; line-height: 17.5px;
    text-align: justify; color: var(--ink);
  }

  .side-photo { position: absolute; left: 426px; width: 79px; }
  .side-photo--gate { top: 113px; height: 123px; background: linear-gradient(180deg, #b9c6cf, #5f7a4a 60%, #3f5a2e); }
  .side-photo--antelope { top: 249px; height: 122px; background: linear-gradient(180deg, #a9a39a, #6e6458 55%, #8ea07a); }
  .side-photo--donkey { top: 386px; height: 123px; background: linear-gradient(180deg, #9fa596, #5e5147 50%, #7f9360); }

  .tagline {
    position: absolute; left: 0; width: 520px; top: 572px; text-align: center;
    font-size: 22px; color: var(--ink);
  }
</style>
</head>
<body>

<section class="page page--amenities">
  <header class="page-title">
    <div class="page-title__band" style="left:0;width:48px"></div>
    <div class="page-title__band" style="left:204px;width:301px"></div>
    <span class="page-title__kicker" style="left:136px">Amenities</span>
    <h1 class="page-title__main" style="left:64px;top:50px">Room</h1>
  </header>

  <div class="watermark" aria-hidden="true">K.L. CREEKSIDE LODGE</div>

  <div class="feature-photo" role="img" aria-label="Guest room bed with red patterned quilt and wooden headboard"></div>
  <p class="feature-item">Plush Bedding</p>

  <div class="amenity" style="left:57px;top:333px">
    <div class="amenity__ring">
      <svg viewBox="0 0 60 60" aria-hidden="true" fill="#3e2a05">
        <rect x="14" y="4" width="9" height="5" rx="1"/>
        <path d="M11 12h15l2 6v32a3 3 0 0 1-3 3H12a3 3 0 0 1-3-3V18z"/>
        <rect x="13" y="26" width="11" height="14" fill="#fff"/>
        <rect x="27" y="38" width="24" height="15" rx="4"/>
        <circle cx="37" cy="30" r="3.5"/><circle cx="45" cy="25" r="3"/><circle cx="45" cy="33" r="2.5"/>
      </svg>
    </div>
    <p class="amenity__label">Shampoo / Soap</p>
  </div>

  <div class="amenity" style="left:185px;top:333px">
    <div class="amenity__ring">
      <svg viewBox="0 0 60 60" aria-hidden="true" fill="none" stroke="#3e2a05" stroke-width="3.5" stroke-linecap="round">
        <path d="M22 6c-3 3 3 5 0 9M30 6c-3 3 3 5 0 9M38 6c-3 3 3 5 0 9" stroke-width="2.5"/>
        <path d="M12 22h32v10a14 14 0 0 1-14 14h-4a14 14 0 0 1-14-14z"/>
        <path d="M44 26h4a5 5 0 0 1 0 10h-5"/>
        <path d="M6 52h44"/>
      </svg>
    </div>
    <p class="amenity__label">Coffee Maker</p>
  </div>

  <div class="amenity" style="left:312px;top:333px">
    <div class="amenity__ring">
      <svg viewBox="0 0 60 60" aria-hidden="true" fill="none" stroke="#3e2a05" stroke-width="5" stroke-linecap="round">
        <path d="M8 24a31 31 0 0 1 44 0"/>
        <path d="M16 32a20 20 0 0 1 28 0"/>
        <path d="M23 40a10 10 0 0 1 14 0"/>
        <circle cx="30" cy="47" r="2.5" fill="#3e2a05" stroke="none"/>
      </svg>
    </div>
    <p class="amenity__label">In Room Wifi</p>
  </div>

  <div class="scene-photo" role="img" aria-label="Stone lodge building with open central breezeway under a cloudy sky"></div>

  <div class="amenity" style="left:185px;top:470px">
    <div class="amenity__ring">
      <svg viewBox="0 0 60 60" aria-hidden="true">
        <path d="M6 18a13 13 0 0 1 13-13h15v26H19A13 13 0 0 1 6 18z" fill="#3e2a05"/>
        <circle cx="19" cy="18" r="5" fill="#fff"/>
        <path d="M16 30h10l-2 24h-8z" fill="#3e2a05"/>
        <path d="M38 10c3 2 6-2 9 0s6-2 9 0M38 18c3 2 6-2 9 0s6-2 9 0M38 26c3 2 6-2 9 0s6-2 9 0" fill="none" stroke="#3e2a05" stroke-width="2.5" stroke-linecap="round"/>
      </svg>
    </div>
    <p class="amenity__label">Hair Dryer</p>
  </div>
</section>

<section class="page page--activities">
  <header class="page-title">
    <div class="page-title__band" style="left:0;width:48px"></div>
    <div class="page-title__band" style="left:194px;width:311px"></div>
    <span class="page-title__kicker" style="left:136px;top:40px">to do while here</span>
    <h1 class="page-title__main" style="left:64px;top:50px">What</h1>
  </header>

  <div class="watermark" aria-hidden="true">K.L. CREEKSIDE LODGE</div>

  <article class="activity" style="top:116px">
    <h2 class="activity__tab">Wildlife Tour</h2>
    <p class="activity__text">View and photograph animals from around the world here at KL Creekside Lodge. Our guides are fun and informative. Be prepared for a fun time.</p>
  </article>

  <article class="activity" style="top:201px">
    <h2 class="activity__tab">Relax by Firepit</h2>
    <p class="activity__text">Have a cocktail and kick your feet up by the fire pit.</p>
  </article>

  <article class="activity" style="top:251px">
    <h2 class="activity__tab">Swim</h2>
    <p class="activity__text">Complete with a waterfall and swim up bar, the K.L. Creekside Lodge pool isa great place to get away from the Texas heat! Too cool to swim? Our hot tub is always on!.</p>
  </article>

  <article class="activity" style="top:339px">
    <h2 class="activity__tab">Hike</h2>
    <p class="activity__text">Start with a shorter loop, tackle tougher terrain or join a guided tour.</p>
  </article>

  <article class="activity" style="top:409px">
    <h2 class="activity__tab">Ride a horse</h2>
    <p class="activity__text">Have you always wanted to ride a horse? Now is your chance! Ask about our guided rides.</p>
  </article>

  <article class="activity" style="top:479px">
    <h2 class="activity__tab activity__tab--wide">Stargazing at Hawk's Ridge</h2>
    <p class="activity__text">Escape city lights and gaze up at views you won't find any&shy;where else!.</p>
  </article>

  <div class="side-photo side-photo--gate" role="img" aria-label="Ranch entrance gate with palm trees"></div>
  <div class="side-photo side-photo--antelope" role="img" aria-label="Blackbuck antelope among shrubs"></div>
  <div class="side-photo side-photo--donkey" role="img" aria-label="Donkey in a grassy field"></div>

  <div class="scene-photo" role="img" aria-label="Stone lodge building with open central breezeway under a cloudy sky"></div>

  <p class="tagline">“a premier wildlife experience”</p>
</section>

</body>
</html>
```